One-Page Flat Design for SEO Company [2 DAYS]

We need a one-page flat design for our SEO company. Our current website is http://www.rankloft.com/. We are looking to completely re-design the site using new flat design techniques.
Below are some examples of the type of style we're going after:
http://quormel.com/
http://tobyrand.co.uk/
https://pentaly.co/
http://milesporter.me/
As you can see- flat, clean, minimal. It is very important you follow this type of style.
For colour scheme, you may use one of the pre-made colour palettes from here:
http://www.vornacle.com/blog/inspiration/24-flat-designs-with-compelling-color-palettes
I've attached a wireframe to be followed.
Hi,

```html
<!DOCTYPE html>
<html lang="en">
<head>
<meta charset="utf-8">
<title>Rank Loft – One Page</title>
<link href="https://fonts.googleapis.com/css2?family=Open+Sans:wght@400;600;700&family=Roboto:wght@300;400;700&family=PT+Sans:wght@400;700&display=swap" rel="stylesheet">
<style>
:root{
  --blue:#3a8fc5;
  --blue-nav:#4792d3;
  --blue-bright:#3f8ee6;
  --cream:#fdfdf0;
  --green:#93c7a1;
  --brown:#65523e;
  --ink:#1f1f1f;
  --muted:#7d7d7d;
  --bronze:#dba27d;--bronze-d:#d98f55;
  --silver:#cacaca;--silver-d:#a8a8a8;
  --gold:#e2c64a;--gold-d:#d4b21c;
  --plat:#8cc2e0;--plat-d:#6aaed6;
  --seal:#7a1c1c;
}
*{box-sizing:border-box;margin:0;padding:0}
html,body{width:1200px;height:3025px;overflow:hidden}
body{position:relative;font-family:"Open Sans",sans-serif;color:var(--ink);background:var(--cream)}
.abs{position:absolute}
.center{left:0;width:1200px;text-align:center}
section,header,footer{position:absolute;left:0;width:1200px}

.topbar{top:0;height:70px;background:var(--blue-nav)}
.brand{left:151px;top:8px;color:#fff}
.brand-name{font-family:"PT Sans",sans-serif;font-size:26px;line-height:30px}
.brand-sub{font-size:11px;line-height:14px}
.nav{right:150px;top:22px;display:flex;gap:0}
.nav a{color:#fff;text-decoration:none;font-family:"Roboto",sans-serif;font-weight:700;font-size:14px;padding:5px 15px}
.nav a.active{background:#2e5c80;border-radius:2px}

.hero{top:70px;height:543px;background:var(--blue)}
.hero h1{top:52px;font-family:"Roboto",sans-serif;font-weight:700;font-size:56px;color:#fff;letter-spacing:-1px}
.hero p{top:138px;font-family:"Roboto",sans-serif;font-weight:300;font-size:19px;line-height:32px;color:#e6f1f8}
.devices{left:345px;top:228px;width:442px;height:252px;background:linear-gradient(#5a5a5a,#8a8a8a);border-radius:6px}

.tab{left:517px;width:151px;height:43px;background:var(--blue-bright);color:#fff;font-family:"Roboto",sans-serif;font-weight:700;font-size:18px;line-height:43px;text-align:center;letter-spacing:1px;z-index:2}
.section-title{font-family:"PT Sans",sans-serif;font-weight:700;font-size:20px}
.lead{font-size:12px;line-height:20px;color:#555}
.feature{width:260px;text-align:center}
.feature h3{font-family:"PT Sans",sans-serif;font-weight:700;font-size:17px;margin-top:0}
.feature p{font-size:12px;line-height:23px;color:var(--muted);margin-top:6px}
.icon-ring{width:112px;height:112px;border-radius:50%;border:7px solid var(--blue);display:flex;align-items:center;justify-content:center;margin:0 auto}

.about{top:613px;height:378px;background:var(--cream)}
.packages{top:991px;height:567px;background:var(--green)}
.plan{text-align:center;background:#fff;font-size:12px}
.plan-head{height:38px;line-height:38px;background:var(--blue);color:#fff;font-family:"PT Sans",sans-serif;font-weight:700;font-size:21px}
.plan-price{height:58px;line-height:58px;font-family:"Roboto",sans-serif;font-weight:700;font-size:34px}
.plan-hi{height:32px;line-height:32px;color:#fff;font-size:11px;border-bottom:1px solid rgba(255,255,255,.35)}
.plan-row{height:32px;line-height:32px;color:#666;font-size:11px;border-bottom:1px solid #e5e5e5;margin:0 14px}
.plan-foot{position:absolute;left:0;bottom:0;width:100%;height:58px;background:var(--blue);display:flex;align-items:center;justify-content:center}
.btn-small{background:#fff;color:var(--blue);font-size:10px;font-weight:700;padding:8px 24px}
.btn-small.dark{background:var(--blue-bright);color:#fff}

.guarantee{top:1558px;height:280px;background:var(--brown);color:#f2ece4}
.guarantee h2{top:25px;font-family:"Roboto",sans-serif;font-weight:700;font-size:19px;color:var(--blue-bright)}
.guarantee p{top:62px;left:190px;width:820px;text-align:center;font-size:11.5px;line-height:23px}

.services{top:1838px;height:386px;background:var(--blue);color:#fff}
.services .feature h3{color:var(--brown)}
.services .feature p{color:#eaf3f9}
.solid-disc{width:136px;height:136px;border-radius:50%;background:var(--green);display:flex;align-items:center;justify-content:center;margin:0 auto}

.contact{top:2224px;height:554px;background:var(--cream)}
.field{border:1px solid #bdbdbd;background:var(--cream);font-size:10px;color:#777;padding:10px 14px}
.send{left:489px;top:405px;width:219px;height:53px;background:var(--blue-bright);color:#fff;font-size:12px;font-weight:600;line-height:53px;text-align:center;letter-spacing:1px}
.socials{top:496px;display:flex;justify-content:center;gap:34px;font-family:"PT Sans",sans-serif;font-weight:700;font-size:18px}

.footer{top:2778px;height:247px;background:var(--brown);color:#fff}
.footer .fname{top:44px;font-family:"PT Sans",sans-serif;font-size:24px}
.footer .fsub{top:72px;font-size:11px}
.footer p{top:108px;font-size:11.5px;line-height:21px;color:#efe8df}
.circles{top:174px;display:flex;justify-content:center;gap:30px}
.circles span{width:46px;height:46px;border-radius:50%;border:2px solid #cfc6ba}
.circles span.on{background:var(--blue-bright);border-color:var(--blue-bright)}
</style>
</head>
<body>

<header class="topbar">
  <div class="abs brand"><div class="brand-name">Rank Loft</div><div class="brand-sub">A single Page Template</div></div>
  <nav class="abs nav"><a class="active">Home</a><a>About</a><a>Packages</a><a>Services</a><a>Other</a><a>Contact</a></nav>
</header>

<section class="hero">
  <h1 class="abs center">Finally, SEO services that actually work.</h1>
  <p class="abs center">Top-notch SEO services that are guaranteed to boost your search engine rankings.<br>100% Seekwell-friendly.</p>
  <div class="abs devices" role="img" aria-label="Laptop, tablet and phone showing the site"></div>
</section>

<div class="abs tab" style="top:595px">ABOUT US</div>
<section class="about">
  <div class="abs center section-title" style="top:50px">Why Choose RankLoft</div>
  <div class="abs feature" style="left:147px;top:108px">
    <div class="icon-ring"><svg width="50" height="40" viewBox="0 0 50 40"><rect x="2" y="2" width="46" height="36" fill="none" stroke="#3a8fc5" stroke-width="4"/><path d="M6 34 L20 18 L30 28 L36 22 L44 34Z" fill="#3a8fc5"/><circle cx="34" cy="12" r="4" fill="#3a8fc5"/></svg></div>
    <h3 style="margin-top:18px">Low Prices</h3><p>Lorem ipsum dolor sit amet, consectetur<br>adipiscing elit. Suspendisse fringilla.</p>
  </div>
  <div class="abs feature" style="left:465px;top:108px">
    <div class="icon-ring"><svg width="50" height="40" viewBox="0 0 50 40"><rect x="2" y="2" width="46" height="36" fill="none" stroke="#3a8fc5" stroke-width="4"/><path d="M6 34 L20 18 L30 28 L36 22 L44 34Z" fill="#3a8fc5"/><circle cx="34" cy="12" r="4" fill="#3a8fc5"/></svg></div>
    <h3 style="margin-top:18px">Increased Ratings</h3><p>Lorem ipsum dolor sit amet, consectetur<br>adipiscing elit. Suspendisse fringilla.</p>
  </div>
  <div class="abs feature" style="left:750px;top:108px">
    <div class="icon-ring"><svg width="50" height="40" viewBox="0 0 50 40"><rect x="2" y="2" width="46" height="36" fill="none" stroke="#3a8fc5" stroke-width="4"/><path d="M6 34 L20 18 L30 28 L36 22 L44 34Z" fill="#3a8fc5"/><circle cx="34" cy="12" r="4" fill="#3a8fc5"/></svg></div>
    <h3 style="margin-top:18px">100% Safe</h3><p>Lorem ipsum dolor sit amet, consectetur<br>adipiscing elit. Suspendisse fringilla.</p>
  </div>
</section>

<div class="abs tab" style="top:978px">SEO PACKAGES</div>
<section class="packages">
  <div class="abs center section-title" style="top:58px;font-size:18px">RankLoft Packages</div>
  <p class="abs center lead" style="top:96px;color:#fff">Lorem ipsum dolor sit amet, pro aeterno adipisci ex, pro no iriure accusam. Eros admodum intellegat ex mea, mei wisi nullam ne, qui cu aliquid<br>nominavi. Est habemus maiestatis ut. Vim quod elitr interesset ex.</p>

  <div class="abs plan" style="left:156px;top:174px;width:220px;height:315px">
    <div class="plan-head">Bronze</div>
    <div class="plan-price" style="background:var(--bronze)">$39</div>
    <div class="plan-hi" style="background:var(--bronze-d)">10 PR5 - PR8 Social Bookmarks</div>
    <div class="plan-hi" style="background:var(--bronze-d)">15 PR5 - PR8 2.0 Profile Backlinks</div>
    <div class="plan-row">One-Way Links</div><div class="plan-row">Delivered within 8 days</div><div class="plan-row" style="border:0">Detailed Submission Report</div>
    <div class="plan-foot"><span class="btn-small">PURCHASE</span></div>
  </div>
  <div class="abs plan" style="left:381px;top:174px;width:216px;height:315px">
    <div class="plan-head">Silver</div>
    <div class="plan-price" style="background:var(--silver)">$58</div>
    <div class="plan-hi" style="background:var(--silver-d)">10 PR5 - PR8 Social Bookmarks</div>
    <div class="plan-hi" style="background:var(--silver-d)">10 PR5-PR8 Web2.0 Profile Backlinks</div>
    <div class="plan-row">One-Way Links</div><div class="plan-row">Delivered within 8 days</div><div class="plan-row" style="border:0">Detailed Submission Report</div>
    <div class="plan-foot"><span class="btn-small">PURCHASE</span></div>
  </div>
  <div class="abs plan" style="left:600px;top:161px;width:219px;height:348px">
    <div class="plan-head" style="height:44px;line-height:44px">Gold</div>
    <div class="plan-price" style="background:var(--gold)">$79</div>
    <div class="plan-hi" style="background:var(--gold-d)">5 PR4 - PR7 LinkWheels</div>
    <div class="plan-hi" style="background:var(--gold-d)">10 PR5 - PR8 Social Bookmarks</div>
    <div class="plan-hi" style="background:var(--gold-d)">10 PR5-PR8 Web2.0 Profile Backlinks</div>
    <div class="plan-row">One-Way Links</div><div class="plan-row">Delivered within 8 days</div><div class="plan-row" style="border:0">Detailed Submission Report</div>
    <div class="plan-foot" style="height:60px"><span class="btn-small dark">PURCHASE</span></div>
  </div>
  <div class="abs plan" style="left:824px;top:174px;width:217px;height:315px">
    <div class="plan-head">Platinum</div>
    <div class="plan-price" style="background:var(--plat)">$139</div>
    <div class="plan-hi" style="background:var(--plat-d)">Full SEO Audit</div>
    <div class="plan-hi" style="background:var(--plat-d)">5 PR4 - PR7 LinkWheels</div>
    <div class="plan-row">One-Way Links</div><div class="plan-row">Delivered within 8 days</div><div class="plan-row" style="border:0">Detailed Submission Report</div>
    <div class="plan-foot"><span class="btn-small">PURCHASE</span></div>
  </div>
</section>

<section class="guarantee">
  <h2 class="abs center">30 DAY MONEY-BACK GUARANTEE</h2>
  <p class="abs">If for whatever reason you are not completely satisfied with our service, we'll refund 100% of your payment without any questions asked within 30 days of your order placement. This money-back guarantee applies to ALL (includes individual SEO and social media listed below) services offered on</p>
  <svg class="abs" style="left:539px;top:118px" width="116" height="116" viewBox="0 0 116 116" role="img" aria-label="Money-back guarantee seal"><circle cx="58" cy="58" r="56" fill="var(--seal)"/><circle cx="58" cy="58" r="38" fill="#8e2a2a" stroke="#b54848" stroke-width="2"/></svg>
</section>

<div class="abs tab" style="top:1815px">SEO SERVICES</div>
<section class="services">
  <div class="abs center section-title" style="top:60px;color:var(--ink)">Individual SEO Services</div>
  <svg class="abs" style="left:128px;top:148px" width="22" height="40" viewBox="0 0 22 40"><path d="M20 2 L3 20 L20 38" fill="none" stroke="#fff" stroke-width="2"/></svg>
  <svg class="abs" style="left:1050px;top:148px" width="22" height="40" viewBox="0 0 22 40"><path d="M2 2 L19 20 L2 38" fill="none" stroke="#fff" stroke-width="2"/></svg>
  <div class="abs feature" style="left:172px;top:100px">
    <div class="solid-disc"><svg width="54" height="44" viewBox="0 0 50 40"><rect x="2" y="2" width="46" height="36" fill="none" stroke="#fff" stroke-width="4"/><path d="M6 34 L20 18 L30 28 L36 22 L44 34Z" fill="#fff"/><circle cx="34" cy="12" r="4" fill="#fff"/></svg></div>
    <h3 style="margin-top:20px">Verified Profile Backlinks</h3><p style="margin-top:2px">Lorem ipsum dolor sit amet, consectetur<br>adipiscing elit. Suspendisse fringilla.</p>
  </div>
  <div class="abs feature" style="left:465px;top:100px">
    <div class="solid-disc"><svg width="54" height="44" viewBox="0 0 50 40"><rect x="2" y="2" width="46" height="36" fill="none" stroke="#fff" stroke-width="4"/><path d="M6 34 L20 18 L30 28 L36 22 L44 34Z" fill="#fff"/><circle cx="34" cy="12" r="4" fill="#fff"/></svg></div>
    <h3 style="margin-top:20px">Blog Comment Backlinks</h3><p style="margin-top:2px">Lorem ipsum dolor sit amet, consectetur<br>adipiscing elit. Suspendisse fringilla.</p>
  </div>
  <div class="abs feature" style="left:767px;top:100px">
    <div class="solid-disc"><svg width="54" height="44" viewBox="0 0 50 40"><rect x="2" y="2" width="46" height="36" fill="none" stroke="#fff" stroke-width="4"/><path d="M6 34 L20 18 L30 28 L36 22 L44 34Z" fill="#fff"/><circle cx="34" cy="12" r="4" fill="#fff"/></svg></div>
    <h3 style="margin-top:20px">PR4 Backlinks</h3><p style="margin-top:2px">Lorem ipsum dolor sit amet, consectetur<br>adipiscing elit. Suspendisse fringilla.</p>
  </div>
</section>

<div class="abs tab" style="top:2200px">CONTACT US</div>
<section class="contact">
  <div class="abs center section-title" style="top:58px;font-size:18px">Feel free to EMAIL US</div>
  <p class="abs center lead" style="top:98px">Lorem ipsum dolor sit amet, pro aeterno adipisci ex, pro no iriure accusam. Eros admodum intellegat ex mea, mei wisi nullam ne, qui cu aliquid nominavi.</p>
  <div class="abs field" style="left:277px;top:148px;width:310px;height:43px">Your Name</div>
  <div class="abs field" style="left:613px;top:148px;width:310px;height:43px">Your Email</div>
  <div class="abs field" style="left:277px;top:211px;width:646px;height:152px">YourMessage</div>
  <div class="abs send">SEND MESSAGE</div>
  <div class="abs center socials"><span>Friendspace</span><span>Chirper</span><span>Circlesy</span><span>Workbond</span></div>
</section>

<footer class="footer">
  <div class="abs center fname">Rank Loft</div>
  <div class="abs center fsub">A single Page Template</div>
  <p class="abs center">Lorem ipsum dolor sit amet, pro aeterno adipisci ex, pro no iriure accusam. Eros admodum intellegat ex mea,<br>mei wisi nullam ne, qui cu aliquid nominavi. Est habemus maiestatis ut. Vim quod elitr interesset ex.</p>
  <div class="abs center circles"><span class="on"></span><span></span><span></span><span></span></div>
</footer>

</body>
</html>
```